Brindlo Wordpress Website

We require a WordPress website that emulates the sleek design and functionality of https://www.quorvexa.com and https://tolmindo.ai/. The site should showcase our AI-powered customer support solutions with a modern, professional aesthetic.
Homepage
The homepage should feature a bold headline highlighting our AI capabilities, followed by concise sections outlining our key offerings:
AI-powered customer support
Data integration and deployment
Knowledge system integration
AI help desks and chat agents
Customer feedback insights
Include eye-catching visuals or animations to illustrate these concepts.
Navigation
The main navigation menu should include:
Product
Platform
Company
News
Learn More
Key Pages
Product Page: Detail our AI solutions, their benefits, and use cases.
Platform Page: Explain our technology, integration capabilities, and deployment process.
Company Page: Share our mission, team, and values.
News Page: Feature latest updates, press releases, and blog posts.
Call-to-Action
Implement a prominent "Learn More" button that directs users to an enrollment page. Our team will manage inquiries from this point.
Footer
Include a "Contact Us" section in the footer for easy access to our contact information.
Design Elements
Use a clean, minimalist design with ample white space
Incorporate a color scheme that reflects trust and innovation
Utilize smooth scrolling and subtle animations for enhanced user experience
Ensure mobile responsiveness for all devices
Technical Requirements
Build on WordPress for easy content management
Optimize for fast loading speeds and SEO
The website should convey our expertise in AI-driven customer support solutions while providing an intuitive user experience that guides visitors toward learning more about our services

```html
<!DOCTYPE html>
<html lang="en">
<head>
<meta charset="utf-8">
<title>Brindlo — AI Customer Support</title>
<link href="https://fonts.googleapis.com/css2?family=Lexend:wght@300;400;500;600;700&display=swap" rel="stylesheet">
<style>
:root{
  --deep:#0b3940;
  --deeper:#082c32;
  --teal:#5b9896;
  --teal-head:#4a8d8b;
  --teal-soft:#e9f3f2;
  --ink:#1d2b2d;
  --muted:#7b8a8c;
  --line:#e3e8e8;
  --paper:#ffffff;
  --mist:#f3f4f4;
  --accent:#e4672b;
}
*{box-sizing:border-box;margin:0;padding:0}
html,body{width:1200px;height:4323px;overflow:hidden}
body{position:relative;font-family:"Lexend",sans-serif;color:var(--ink);background:var(--paper)}
.abs{position:absolute}
.brand{display:flex;align-items:center;gap:10px;color:#fff;font-weight:500;font-size:29px}
.brand .dot{width:40px;height:40px;border-radius:50%;background:var(--teal)}
/* hero */
.hero{left:0;top:0;width:1200px;height:1100px}
.nav{left:508px;top:34px;display:flex;gap:17px;font-size:13px;color:#fff}
.nav .on{color:var(--teal)}
.call{left:925px;top:28px;display:flex;align-items:center;gap:10px;color:#fff}
.call .ring{width:32px;height:32px;border-radius:50%;background:var(--teal);display:flex;align-items:center;justify-content:center}
.call small{display:block;font-size:8px;letter-spacing:.5px}
.call b{font-size:13px;font-weight:600}
.hero-title{left:0;width:1200px;top:205px;text-align:center;color:var(--teal);font-weight:700;font-size:34px;line-height:38px}
.hero-sub{left:0;width:1200px;top:298px;text-align:center;color:#fff;font-size:15px}
.btn{display:flex;align-items:center;justify-content:center;border-radius:20px;color:#fff;font-size:13px}
.btn-demo{left:520px;top:342px;width:160px;height:34px;background:var(--teal)}
.tabs{left:151px;top:708px;width:186px}
.tab{height:80px;display:flex;align-items:center;gap:12px;padding-left:12px;color:#7f9a9d;border-bottom:1px solid #1d4c53;font-size:15px;line-height:18px}
.tab .n{font-size:22px;font-weight:300}
.tab.on{background:var(--teal);color:#fff}
.chat{left:426px;top:660px;width:581px;height:337px;background:#fff;border-radius:4px;overflow:hidden;font-size:9px}
.chat-main{position:absolute;left:0;top:0;width:400px;height:100%;border-right:1px solid var(--line)}
.chat-top{height:40px;background:#f3f6fb;padding:8px 12px;display:flex;justify-content:space-between}
.chat-top b{font-size:11px}
.bubble{position:absolute;left:12px;top:66px;background:#f1f2f3;border-radius:10px;padding:5px 10px;color:#444}
.chat-input{position:absolute;left:12px;bottom:16px;width:340px;height:28px;background:#f3f5f8;border-radius:4px;padding:8px 10px;color:#999}
.send{position:absolute;right:14px;bottom:16px;width:28px;height:28px;border-radius:4px;background:#fbe9e1}
.side{position:absolute;left:410px;top:8px;width:160px}
.side .h{font-weight:600;margin:0 0 10px}
.item{display:flex;gap:10px;margin-bottom:14px}
.item i{width:22px;height:22px;border-radius:6px;background:#e7eefc;flex:none}
.item.c i{border-radius:50%;background:#c9a48f}
.item b{display:block;font-size:8px;font-weight:600}
.item span{font-size:7px;color:#999}
/* sections */
.h2{left:0;width:1200px;text-align:center;color:var(--teal-head);font-weight:500;font-size:22px}
.logos{left:218px;width:764px;display:flex;justify-content:space-between;align-items:center;font-size:26px;font-weight:600;color:#1e1e1e}
.logos span{display:flex;align-items:center;gap:6px}
.logos .sq{width:24px;height:24px;border-radius:50%;background:#1e1e1e}
.card{width:250px;height:254px;background:#fff;border-radius:16px;box-shadow:0 4px 24px rgba(0,0,0,.08);text-align:center;padding-top:56px}
.card .ic{width:70px;height:70px;margin:0 auto 18px}
.card b{display:block;font-weight:500;font-size:14px;margin-bottom:12px}
.card p{font-size:11px;color:var(--muted);line-height:16px;padding:0 36px}
.feat{left:612px;width:450px}
.feat .row{display:flex;gap:18px;margin-bottom:34px}
.feat .fi{width:40px;height:40px;flex:none}
.feat h3{color:var(--teal-head);font-weight:500;font-size:14px;line-height:17px;margin-bottom:6px}
.feat li{list-style:none;font-size:10.5px;line-height:14px;margin-bottom:7px;padding-left:14px;position:relative}
.feat li:before{content:"";position:absolute;left:0;top:3px;width:7px;height:7px;border-radius:50%;background:#cfe1e0}
.para{left:240px;width:720px;text-align:center;font-size:11px;line-height:14px}
.acc{left:200px;width:354px;height:101px;border-radius:8px;background:#f3f9f9;padding:22px 18px;font-size:11px;line-height:14px}
.acc b{display:block;color:var(--teal-head);font-weight:500;font-size:12px;margin-bottom:8px}
.acc p{color:#3f4b4d}
.acc.on{background:var(--teal)}
.acc.on b{color:#fff}.acc.on p{color:#d9ecea}
.preview{left:612px;top:2489px;width:378px;height:347px;background:#fff;box-shadow:0 2px 14px rgba(0,0,0,.07);border-radius:8px;overflow:hidden;font-size:8px}
.preview .top{height:125px;background:#fdf8f1;padding:14px}
.preview .q{margin-top:20px;background:#fff;border-radius:4px;padding:8px;display:flex;justify-content:space-between;align-items:center}
.preview .go{width:18px;height:18px;border-radius:50%;background:#d6651f}
.preview ul{padding:14px 14px 0 28px;line-height:16px}
.stars{left:235px;top:3074px;color:var(--teal);font-size:16px;letter-spacing:2px}
.stars small{font-size:11px;letter-spacing:0;margin-left:6px}
.quote{left:235px;top:3118px;width:500px;font-size:18px;line-height:24px;font-weight:300}
.form input,.form textarea{position:absolute;border:1px solid #d9dcdc;background:#fff;font-family:inherit;font-size:10px;padding:8px 12px;color:#999}
.foot h4{color:var(--teal);font-weight:500;font-size:15px;margin-bottom:18px}
.foot p,.foot a{display:block;color:#fff;font-size:11px;line-height:15px;text-decoration:none;margin-bottom:7px}
.social{display:flex;gap:10px}
.social i{width:14px;height:14px;border-radius:50%;background:#fff;display:block}
</style>
</head>
<body>

<!-- HERO -->
<svg class="abs hero" viewBox="0 0 1200 1100" aria-hidden="true">
  <defs><linearGradient id="hg" x1="0" y1="0" x2="0" y2="1"><stop offset="0" stop-color="#0d3f45"/><stop offset="1" stop-color="#082e34"/></linearGradient></defs>
  <path d="M0 0H1200V1050Q600 1140 0 1050Z" fill="url(#hg)"/>
  <path d="M0 470Q600 330 1200 470V540Q600 410 0 540Z" fill="#1b4e55" opacity=".55"/>
  <path d="M0 520Q600 380 1200 520" stroke="#2b6068" stroke-width="2" fill="none"/>
</svg>
<div class="abs brand" style="left:150px;top:22px"><span class="dot"></span>Brindlo</div>
<nav class="abs nav"><span class="on">Home</span><span>Product</span><span>Platform</span><span>Company</span><span>News</span><span>Contact Us</span></nav>
<div class="abs call"><span class="ring"><svg width="14" height="14" viewBox="0 0 24 24"><path fill="#fff" d="M6.6 10.8a15 15 0 006.6 6.6l2.2-2.2a1 1 0 011-.25 11.4 11.4 0 003.6.6 1 1 0 011 1V20a1 1 0 01-1 1A17 17 0 013 4a1 1 0 011-1h3.5a1 1 0 011 1 11.4 11.4 0 00.6 3.6 1 1 0 01-.25 1z"/></svg></span><span><small>CALL NOW</small><b>555.010.2048</b></span></div>
<h1 class="abs hero-title">Enhance your customer experience<br>with Brindlo's AI Assistant.</h1>
<p class="abs hero-sub">Always ready, always on - 24/7</p>
<div class="abs btn btn-demo">Request a Demo</div>

<div class="abs tabs">
  <div class="tab on"><span class="n">01</span>Ticket<br>Deflection<span style="margin-left:auto;margin-right:18px;font-size:20px">›</span></div>
  <div class="tab"><span class="n">02</span>Agent<br>Assist</div>
  <div class="tab"><span class="n">03</span>Reporting<br>and Insights</div>
</div>

<div class="abs chat">
  <div class="chat-main">
    <div class="chat-top"><div><b>ChatBot</b><br><span style="font-size:7px;color:#888">Talk to AI chatbot about anything</span></div><div style="font-size:8px;padding-top:6px">3.5 ▾ &nbsp; <span style="border:1px solid #ccc;border-radius:4px;padding:2px 6px">Clear</span></div></div>
    <div class="bubble">Hello! How can I help you today?</div>
    <div class="chat-input">Enter Message</div><div class="send"></div>
  </div>
  <div class="side">
    <div class="h">Tools</div>
    <div class="item"><i></i><div><b>Paragraph Writer</b><span>Generate well-written...</span></div></div>
    <div class="item"><i></i><div><b>Essay Writer</b><span>Create essays your way...</span></div></div>
    <div class="item"><i></i><div><b>Text Summarizer</b><span>Shorten text with AI...</span></div></div>
    <div class="item"><i></i><div><b>AI Text Rewriter</b><span>Easily rewrite text to...</span></div></div>
    <div class="h">Characters</div>
    <div class="item c"><i></i><div><b>Mira</b><span>Mira, your friendly guide...</span></div></div>
    <div class="item c"><i></i><div><b>Talia</b><span>Talia, your poised mentor...</span></div></div>
    <div class="item c"><i></i><div><b>Owen</b></div></div>
  </div>
</div>

<!-- TRUSTED -->
<h2 class="abs h2" style="top:1168px">Trusted By Enterprises</h2>
<div class="abs logos" style="top:1226px"><span><i class="sq"></i>Voyastra</span><span>Leadnest</span><span>Taskora</span><span>Fenwy</span><span>Pulsive</span></div>
<div class="abs" style="left:200px;top:1326px;width:800px;height:1px;background:var(--line)"></div>

<!-- REVOLUTIONIZE -->
<h2 class="abs h2" style="top:1394px">Revolutionize your customer interactions:</h2>
<div class="abs card" style="left:200px;top:1446px"><svg class="ic" viewBox="0 0 70 70"><circle cx="44" cy="26" r="18" fill="none" stroke="#1e3b40" stroke-width="2.5"/><circle cx="24" cy="46" r="14" fill="var(--teal)"/><text x="44" y="32" font-size="16" text-anchor="middle" fill="#1e3b40" font-family="Lexend">A</text><text x="24" y="52" font-size="14" text-anchor="middle" fill="#fff" font-family="Lexend">Q</text></svg><b>Get answers</b><p>Users will find the information they need in seconds</p></div>
<div class="abs card" style="left:475px;top:1446px"><svg class="ic" viewBox="0 0 70 70"><circle cx="35" cy="20" r="9" fill="var(--teal)"/><circle cx="20" cy="44" r="7" fill="none" stroke="#1e3b40" stroke-width="2.5"/><circle cx="50" cy="44" r="7" fill="none" stroke="#1e3b40" stroke-width="2.5"/><path d="M8 66q12-16 24 0M38 66q12-16 24 0" fill="none" stroke="#1e3b40" stroke-width="2.5"/></svg><b>Solve problems</b><p>Concerns will be addressed quickly with expert assistance</p></div>
<div class="abs card" style="left:750px;top:1446px"><svg class="ic" viewBox="0 0 70 70"><circle cx="35" cy="35" r="24" fill="none" stroke="#1e3b40" stroke-width="3"/><circle cx="35" cy="35" r="12" fill="var(--teal)"/><path d="M35 4v14M35 52v14M4 35h14M52 35h14" stroke="#1e3b40" stroke-width="3"/></svg><b>Take action</b><p>Users will activate services and features immediately</p></div>
<p class="abs" style="left:0;width:1200px;top:1730px;text-align:center;font-size:13px">All through natural, conversational experiences.</p>

<!-- FEATURES -->
<svg class="abs" style="left:0;top:1810px" width="1200" height="490" aria-hidden="true"><path d="M0 40Q600 -30 1200 40V440Q600 520 0 440Z" fill="var(--mist)"/></svg>
<div class="abs" role="img" aria-label="Photo of a smiling woman working on a laptop beside a friendly robot assistant" style="left:175px;top:1885px;width:362px;height:362px;border-radius:50%;background:radial-gradient(circle at 40% 40%,#e9e4dc,#9fb6bd)"></div>
<div class="abs" style="left:415px;top:2140px;width:105px;height:105px;border-radius:50%;background:var(--teal)"></div>
<div class="abs feat" style="top:1905px">
  <div class="row"><svg class="fi" viewBox="0 0 40 40"><circle cx="18" cy="18" r="14" fill="none" stroke="#1e3b40" stroke-width="2"/><circle cx="30" cy="30" r="7" fill="var(--teal)"/></svg><div><h3>Brindlo enables you to:</h3><ul><li>Engage and delight customers with an AI agent aligned to your brand</li><li>Provide real-time support for a wide variety of uses from simple to complex</li></ul></div></div>
  <div class="row"><svg class="fi" viewBox="0 0 40 40"><rect x="9" y="9" width="22" height="22" rx="3" fill="none" stroke="#1e3b40" stroke-width="2"/><rect x="14" y="14" width="12" height="12" fill="var(--teal)"/><path d="M15 2v7M25 2v7M15 31v7M25 31v7M2 15h7M2 25h7M31 15h7M31 25h7" stroke="#1e3b40" stroke-width="2"/></svg><div><h3>Make AI your own with Brindlo's<br>conversational platform:</h3><ul><li>Engage and delight customers with an AI agent aligned to your brand</li><li>Provide real-time support for a wide variety of uses from simple to complex</li></ul></div></div>
  <div class="row"><svg class="fi" viewBox="0 0 40 40"><path d="M20 4l10 4v9c0 6-4 10-10 12-6-2-10-6-10-12V8z" fill="var(--teal)"/><path d="M4 22v10l8 6M36 22v10l-8 6" fill="none" stroke="#1e3b40" stroke-width="2"/></svg><div><h3>Brindlo prioritizes trust and security:</h3><ul><li>Built-in supervision and auditing</li><li>Secure integrations</li><li>Strong data governance and privacy</li></ul></div></div>
</div>

<!-- SUPPORT -->
<h2 class="abs h2" style="top:2386px">Faster, more personal customer support</h2>
<p class="abs para" style="top:2424px">Lorem Ipsum is simply dummy text of the printing and typesetting industry. Lorem Ipsum has been the industry's standard dummy text ever since the 1500s, when an unknown printer took a galley of type and scrambled it to make a type specimen book.</p>
<div class="abs acc on" style="top:2489px"><b>Lorem Ipsum is simply dummy text of the printing industry.</b><p>Lorem Ipsum has been the industry's standard dummy text ever since the 1500s, when an unknown...</p></div>
<div class="abs acc" style="top:2612px"><b>Lorem Ipsum is simply dummy text of the printing industry.</b><p>Lorem Ipsum has been the industry's standard dummy text ever since the 1500s, when an unknown...</p></div>
<div class="abs acc" style="top:2735px"><b>Lorem Ipsum is simply dummy text of the printing industry.</b><p>Lorem Ipsum has been the industry's standard dummy text ever since the 1500s, when an unknown...</p></div>
<div class="abs preview">
  <div class="top"><span style="display:inline-block;width:16px;height:16px;border-radius:50%;background:#b7c6e0"></span>
    <div class="q">How do I promote my July wine tour?<span class="go"></span></div>
    <div style="text-align:right;margin-top:8px;font-size:6px">Powered by Quorvexa</div></div>
  <ul><li>Social Media Post #1 (Post on Wednesday at 5 PM)<ul><li>Content: Share a stunning image of your vineyard with a teaser about the upcoming event.</li><li>Caption: 'Something special is brewing in the heart of the valley. Stay tuned for our wine tour announcement!'</li></ul></li></ul>
  <div style="padding:10px 14px 0;line-height:14px"><b>One Week Before the Event:</b><ul style="padding:0 0 0 14px"><li>Email Reminder (Send on Monday at 9 AM)<ul><li>Subject: 'Don't Miss Out: Exclusive Midday Wine Tour!'</li></ul></li></ul></div>
</div>
<div class="abs btn" style="left:522px;top:2875px;width:148px;height:34px;background:var(--deep)">View Solutions</div>

<!-- TESTIMONIAL -->
<svg class="abs" style="left:0;top:2990px" width="1200" height="390" aria-hidden="true"><path d="M0 30Q600 -20 1200 30V340Q600 400 0 340Z" fill="var(--mist)"/></svg>
<div class="abs stars">★★★★★<small>4.5</small></div>
<p class="abs quote">Lorem Ipsum is simply dummy text of the printing and typesetting industry. Lorem Ipsum has been the industry's standard dummy text ever since the 1500s, when an unknown printer took a galley of type and scrambled it to make a type specimen book.</p>
<div class="abs" style="left:170px;top:3150px;display:flex;flex-direction:column;gap:10px"><i style="width:7px;height:7px;border:1px solid #bbb;border-radius:50%"></i><i style="width:7px;height:7px;border:1px solid #bbb;border-radius:50%"></i><i style="width:7px;height:7px;background:var(--teal);border-radius:50%"></i><i style="width:7px;height:7px;border:1px solid #bbb;border-radius:50%"></i></div>
<svg class="abs" style="left:235px;top:3272px" width="46" height="32" aria-hidden="true"><path d="M18 4Q2 14 6 26Q14 32 18 22M40 4Q24 14 28 26Q36 32 40 22" fill="none" stroke="var(--teal)" stroke-width="1.5"/></svg>
<div class="abs" style="left:294px;top:3280px;font-size:12px;line-height:16px"><b style="color:var(--teal-head);font-weight:500">Daniel Morrow</b><br>Head of Data and AI at Voyastra</div>
<div class="abs" style="left:810px;top:3092px;width:202px;height:202px;border-radius:50%;background:#fff;display:flex;align-items:center;justify-content:center;gap:6px;font-size:24px;font-weight:600"><i style="width:20px;height:20px;border-radius:50%;background:#1e1e1e"></i>Voyastra</div>

<!-- INTEGRATIONS -->
<h2 class="abs h2" style="top:3476px">Seamless Integrations</h2>
<div class="abs logos" style="top:3533px"><span><i class="sq"></i>Voyastra</span><span>Leadnest</span><span>Taskora</span><span>Fenwy</span><span>Pulsive</span></div>

<!-- CONTACT + FOOTER -->
<svg class="abs" style="left:0;top:3630px" width="1200" height="693" aria-hidden="true">
  <path d="M0 30Q600 -20 1200 30V693H0Z" fill="var(--mist)"/>
  <path d="M0 430Q400 320 900 360Q1080 380 1200 340V693H0Z" fill="#b9c8c9"/>
  <path d="M0 450Q450 350 1200 380V693H0Z" fill="var(--deep)"/>
  <rect y="655" width="1200" height="38" fill="var(--deeper)"/>
</svg>
<h2 class="abs" style="left:150px;top:3730px;color:var(--teal-head);font-weight:500;font-size:22px;line-height:27px">Ready to take the first<br>step transforming your<br>customer support?</h2>
<p class="abs" style="left:150px;top:3820px;width:360px;font-size:10px;line-height:14px;color:#3f4b4d">Lorem Ipsum is simply dummy text of the printing and typesetting industry. Lorem Ipsum has been the industry's standard dummy text ever since the 1500s, when an unknown printer took a galley of type and scrambled it to make a type specimen book.</p>
<div class="form">
  <input style="left:609px;top:3730px;width:210px;height:32px" value="Full Name" readonly>
  <input style="left:609px;top:3768px;width:210px;height:32px" value="Email" readonly>
  <input style="left:609px;top:3806px;width:210px;height:32px" value="Phone" readonly>
  <textarea style="left:834px;top:3730px;width:210px;height:108px" readonly>Message</textarea>
</div>
<div class="abs btn" style="left:609px;top:3873px;width:106px;height:34px;background:var(--deep)">Submit</div>

<div class="abs brand" style="left:150px;top:4128px"><span class="dot"></span>Brindlo</div>
<div class="abs foot" style="left:390px;top:4077px"><h4>Conatct info</h4><p>⌖ &nbsp;Lorem Ipsum, Avalon Ridge 00412<br>&nbsp;&nbsp;&nbsp;&nbsp;United States</p><p>✆ &nbsp;1-800-555-0139</p><p>✉ &nbsp;hello@brindlo.com</p><p>◎ &nbsp;Live location</p></div>
<div class="abs foot" style="left:637px;top:4077px"><h4>Quick Link</h4><a style="color:var(--teal);text-decoration:underline">Home</a><a>Product</a><a>Platform</a><a>Company</a><a>News</a><a>Contact Us</a></div>
<div class="abs foot" style="left:812px;top:4077px;width:240px"><h4>Stay In Touch</h4><p>Subscribe to our newsletter and stay updated</p>
  <div style="margin-top:8px;width:238px;height:30px;border:1px solid #5e7d80;border-radius:15px;color:#9ab;font-size:10px;padding:8px 14px">Your email address*</div>
  <div class="btn" style="margin-top:12px;width:104px;height:32px;background:var(--teal)">Submit</div></div>
<p class="abs" style="left:150px;top:4298px;color:#fff;font-size:10px">© 2024 Brindlo. All Right Reserved</p>
<div class="abs social" style="left:915px;top:4298px"><i></i><i></i><i></i><i></i><i></i></div>
</body>
</html>
```